Stationery and Business Card Design

We need stationary design for our new company larkvale. Larkvale is a company that provides city apartment rentals for tourists in Athens We need business cards, letterheads for A4 and A5 and envelopes for A4 A5. The design needs to be modern, friendly and corporate.

Target Market(s)

City Tourists

Industry/Entity Type

Tourism

```html
<!DOCTYPE html>
<html lang="en">
<head>
<meta charset="utf-8">
<title>Larkvale Apartments — Stationery</title>
<link rel="stylesheet" href="https://fonts.googleapis.com/css2?family=Montserrat:wght@300;400;600&family=Tinos:ital@0;1&display=swap">
<style>
:root{
  --brand:#8d0052;
  --brand-dark:#7a0047;
  --ink:#333;
  --paper:#fff;
  --tint:#f3e4ec;
  --bg-top:#5e5e5e;
  --bg-bottom:#454545;
}
*{margin:0;padding:0;box-sizing:border-box}
html,body{width:1200px;height:1200px;overflow:hidden}
body{background:linear-gradient(var(--bg-top),var(--bg-bottom));position:relative;font-family:"Montserrat",sans-serif;color:var(--ink)}
.sheet{position:absolute;background:var(--paper);overflow:hidden}
.brand{position:absolute;text-align:center;color:var(--brand)}
.brand-square{display:block;margin:0 auto;background:var(--brand)}
.brand-name{display:block;font-weight:300;line-height:1;white-space:nowrap}
.contact{position:absolute;font-size:6.4px;line-height:1}
.contact p{white-space:nowrap}
.contact .row{display:flex;align-items:center;gap:12px;height:10.5px}
.contact svg{width:7px;height:7px;fill:none;stroke:var(--brand);stroke-width:1.6}
.gap{height:7px}
.tint-block{position:absolute;background:linear-gradient(rgba(243,228,236,0),var(--tint))}

/* letterhead */
.letterhead{left:66px;top:180px;width:482px;height:682px}
.letter{position:absolute;left:60px;top:133px;width:358px;font-family:"Tinos",serif;font-size:9.4px;line-height:11.7px;color:#222}
.letter p{text-align:justify;margin-bottom:11.7px}
.letter .close{text-align:left;margin-top:52px;margin-bottom:0}
.signature{width:70px;height:26px;margin:3px 0 3px -4px;background:linear-gradient(90deg,#e6e6e6,#f4f4f4)}

/* envelope */
.envelope{left:631px;top:180px;width:495px;height:700px}
.envelope-flap{position:absolute;left:0;top:0}

/* blank sheet */
.blank-sheet{left:578px;top:261px;width:496px;height:701px}

/* cards */
.card{top:881px;width:234px;height:130px}
.card-front{left:66px}
.card-back{left:313px}
.card-person{position:absolute;left:116px;top:26px}
.card-person .name{font-size:7.5px;font-weight:600;color:#222}
.card-person .role{font-size:5.2px;color:var(--brand);margin-top:3px}
.card-contact{font-size:5.2px}
.card-contact .row{height:8.2px;gap:10px}
.card-contact svg{width:5.5px;height:5.5px}
</style>
</head>
<body>
<svg width="0" height="0" style="position:absolute">
  <defs>
    <symbol id="icon-phone" viewBox="0 0 10 10"><path d="M1 3.5 Q5 0.5 9 3.5 M2.5 4 L7.5 4 L8.5 8.5 L1.5 8.5 Z"/></symbol>
    <symbol id="icon-mobile" viewBox="0 0 10 10"><rect x="2.5" y="0.8" width="5" height="8.4" rx="0.8"/></symbol>
    <symbol id="icon-mail" viewBox="0 0 10 10"><rect x="0.8" y="2" width="8.4" height="6"/><path d="M0.8 2 L5 5.5 L9.2 2"/></symbol>
    <symbol id="icon-web" viewBox="0 0 10 10"><circle cx="5" cy="5" r="4"/><path d="M1 5 H9 M5 1 Q2.5 5 5 9 M5 1 Q7.5 5 5 9"/></symbol>
  </defs>
</svg>

<!-- envelope (behind) -->
<section class="sheet envelope" aria-label="Envelope">
  <svg class="envelope-flap" width="495" height="140" viewBox="0 0 495 140">
    <path d="M0 0 H495 L470 100 Q462 132 436 132 H30 Z" fill="var(--brand)"/>
  </svg>
  <div class="brand" style="left:0;width:495px;top:18px">
    <span class="brand-square" style="width:28px;height:28px;background:#fff"></span>
    <span class="brand-name" style="font-size:19px;color:#fff;margin-top:6px">Larkvale</span>
  </div>
</section>

<!-- blank letterhead -->
<section class="sheet blank-sheet" aria-label="Blank letterhead">
  <div class="brand" style="left:29px;width:130px;top:39px">
    <span class="brand-square" style="width:30px;height:30px"></span>
    <span class="brand-name" style="font-size:20px;margin-top:8px">Larkvale</span>
  </div>
  <div class="contact" style="left:202px;top:222px;left:202px"></div>
  <div class="contact" style="left:202px;top:0;display:none"></div>
  <div class="contact" style="left:202px"></div>
  <div class="contact" style="left:46px;top:129px">
    <p style="height:10px">14 Orchard Lane, Kifisia</p>
    <p>Athens 145 62</p>
    <div class="gap"></div>
    <div class="row"><svg><use href="#icon-phone"/></svg><span>210 555 0142</span></div>
    <div class="row"><svg><use href="#icon-mail"/></svg><span>info@larkvaleapartments.com</span></div>
    <div class="row"><svg><use href="#icon-web"/></svg><span>www.larkvaleapartments.com</span></div>
  </div>
  <div class="tint-block" style="left:260px;top:469px;width:200px;height:232px"></div>
</section>

<!-- letterhead with letter -->
<section class="sheet letterhead" aria-label="Letterhead">
  <div class="brand" style="left:42px;width:130px;top:22px">
    <span class="brand-square" style="width:31px;height:31px"></span>
    <span class="brand-name" style="font-size:20px;margin-top:8px">Larkvale</span>
  </div>
  <div class="contact" style="left:297px;top:30px">
    <p style="height:10px">14 Orchard Lane, Kifisia</p>
    <p>Athens 145 62</p>
    <div class="gap"></div>
    <div class="row"><svg><use href="#icon-phone"/></svg><span>210 555 0142</span></div>
    <div class="row"><svg><use href="#icon-mail"/></svg><span>info@larkvaleapartments.com</span></div>
    <div class="row"><svg><use href="#icon-web"/></svg><span>www.larkvaleapartments.com</span></div>
  </div>
  <div class="tint-block" style="left:237px;top:452px;width:233px;height:230px"></div>
  <article class="letter">
    <p>Gentlemen,</p>
    <p>Enclosed I have the honor to send you an article which I should be pleased if you would accept for the "Harbour Review". I am <em>desperately</em> pushed for money; and in the event of Mr. Hallorann's liking the "Landscape-Garden", I would take it as an especial favor if you would mail me the amount due for it, so as to reach me here by the 21st, on which day I shall need it. Can you possibly oblige me in this? If you accept the paper I presume you will allow me your usual sum, whatever that is for similar contributions—but I set no price—leaving all to your own liberality. The piece will make 8 of your pages and rather more.</p>
    <p>Will you be kind enough to put the best possible interpretation upon my behavior while in the city? You must have conceived a <em>queer</em> idea of me—but the simple truth is that Whitcombe would insist upon <em>the juleps</em>, and I knew not what I was either doing or saying. The Review of Fenwick which I offered you was deficient in a 1/2 page of commencement, which I had written to supersede the old beginning, and which gave the article the character of a general and retrospective review. No wonder you did not take it—I would have been very much mortified if you had. I hope to see you at some future time, under better auspices.</p>
    <p class="close">In the meantime I remain<br>Yours very truly,</p>
    <div class="signature" role="img" aria-label="Handwritten signature"></div>
    <p style="margin:0;text-align:left">Elias Marren</p>
  </article>
</section>

<!-- business card front -->
<section class="sheet card card-front" aria-label="Business card, front">
  <div class="brand" style="left:17px;width:90px;top:45px">
    <span class="brand-square" style="width:20px;height:20px"></span>
    <span class="brand-name" style="font-size:14px;margin-top:5px">Larkvale</span>
  </div>
  <div class="card-person">
    <p class="name">Nikos Arvanitis</p>
    <p class="role">President</p>
  </div>
  <div class="contact card-contact" style="left:116px;top:52px">
    <p style="height:8px">14 Orchard Lane, Kifisia</p>
    <p>Athens 145 62</p>
    <div style="height:5px"></div>
    <div class="row"><svg><use href="#icon-phone"/></svg><span>210 555 0142</span></div>
    <div class="row"><svg><use href="#icon-mobile"/></svg><span>210 555 0148</span></div>
    <div class="row"><svg><use href="#icon-mail"/></svg><span>info@larkvaleapartments.com</span></div>
    <div class="row"><svg><use href="#icon-web"/></svg><span>www.larkvaleapartments.com</span></div>
  </div>
</section>

<!-- business card back -->
<section class="sheet card card-back" aria-label="Business card, back">
  <div class="brand" style="left:0;width:234px;top:40px">
    <span class="brand-square" style="width:25px;height:25px"></span>
    <span class="brand-name" style="font-size:17px;margin-top:6px">Larkvale</span>
  </div>
</section>
</body>
</html>
```